Business Card

THIS IS THE CARD INFORMATION
DEVELOPMENT I FINANCING I PROPERTY MANAGEMENT
DANIEL FERRÁN
3186 NE 74th Terrace
Bay Meadows, FL 33412
Telephone I 855.274.6180
Facsimile I 855.274.6127
Industry/Entity Type
Business

```html
<!DOCTYPE html>
<html lang="en">
<head>
<meta charset="utf-8">
<title>Ortega Vidal &amp; Company – Business Card</title>
<link href="https://fonts.googleapis.com/css2?family=Open+Sans:wght@300;400;600;700;800&display=swap" rel="stylesheet">
<style>
  :root {
    --purple: #8e1f7f;
    --purple-deep: #6f1763;
    --ink: #1b1b1b;
    --grey: #555555;
    --paper: #ffffff;
    --backdrop: #e7e4df;
    --band-dark: #1f1f1f;
  }
  * { margin: 0; padding: 0; box-sizing: border-box; }
  html, body {
    width: 1200px;
    height: 1023px;
    overflow: hidden;
    background: var(--backdrop);
    font-family: "Open Sans", Arial, sans-serif;
  }
  .card {
    position: absolute;
    left: 75px;
    top: 211px;
    width: 1050px;
    height: 600px;
    background: var(--paper);
    box-shadow: 0 10px 30px rgba(0,0,0,0.18);
    overflow: hidden;
  }
  .brand {
    position: absolute;
    left: 60px;
    top: 150px;
    display: flex;
    align-items: center;
    gap: 18px;
  }
  .brand-dot {
    width: 80px;
    height: 80px;
    border-radius: 50%;
    background: var(--purple);
    flex: none;
  }
  .brand-text {
    display: flex;
    flex-direction: column;
    align-items: flex-end;
  }
  .brand-name {
    font-weight: 800;
    font-size: 50px;
    line-height: 1;
    letter-spacing: 0.5px;
    color: var(--ink);
    text-transform: uppercase;
  }
  .brand-suffix {
    margin-top: 4px;
    font-weight: 800;
    font-size: 19px;
    line-height: 1;
    color: var(--purple);
    text-transform: uppercase;
  }
  .divider {
    position: absolute;
    left: 330px;
    right: 60px;
    top: 300px;
    height: 3px;
    background: var(--purple);
  }
  .person-name {
    position: absolute;
    right: 60px;
    top: 254px;
    font-weight: 700;
    font-size: 28px;
    line-height: 38px;
    color: var(--purple);
    letter-spacing: 0.5px;
  }
  .person-title {
    position: absolute;
    right: 60px;
    top: 312px;
    font-weight: 400;
    font-size: 20px;
    color: var(--grey);
    letter-spacing: 1px;
  }
  .contact {
    position: absolute;
    left: 330px;
    top: 348px;
    font-weight: 300;
    font-size: 25px;
    line-height: 36px;
    color: var(--grey);
    list-style: none;
  }
  .contact .label { color: var(--purple); font-weight: 400; }
  .band {
    position: absolute;
    left: 0;
    bottom: 0;
    width: 100%;
    height: 62px;
    display: flex;
  }
  .band-services {
    flex: 0 0 73%;
    background: linear-gradient(var(--purple), var(--purple-deep));
    color: var(--paper);
    font-size: 21px;
    letter-spacing: 1px;
    display: flex;
    align-items: center;
    padding-left: 34px;
    text-transform: uppercase;
  }
  .band-accent {
    flex: 1;
    background: var(--band-dark);
  }
</style>
</head>
<body>
  <section class="card" aria-label="Business card front">
    <div class="brand">
      <span class="brand-dot"></span>
      <div class="brand-text">
        <span class="brand-name">Ortega Vidal</span>
        <span class="brand-suffix">&amp; Company</span>
      </div>
    </div>

    <p class="person-name">DANIEL FERRÁN</p>
    <div class="divider"></div>
    <p class="person-title">JOB TITLE</p>

    <ul class="contact">
      <li><span class="label">T</span> : 855.274.6180</li>
      <li><span class="label">F</span> : 855.274.6127</li>
      <li>3186 NE 74th Terrace</li>
      <li>Bay Meadows, FL 33412</li>
    </ul>

    <div class="band">
      <div class="band-services">Development | Financing | Property Management</div>
      <div class="band-accent"></div>
    </div>
  </section>
</body>
</html>
```